Tandrel needs stationery design

We need desings for presentation cards and letter head for our company. It would be better that the letterhead uses our logo with white background and the presentation card the logo with the black background for the back of the card and the text (name, phone

Colors
0455a3
ec1f27
000000

Requirements
Must have
• Use company logo and colors

```html
<!DOCTYPE html>
<html lang="en">
<head>
<meta charset="utf-8">
<title>Tandrel Business Card</title>
<link href="https://fonts.googleapis.com/css2?family=Open+Sans:wght@400;600;700&display=swap" rel="stylesheet">
<style>
  :root {
    --brand-blue: #0455a3;
    --brand-red: #ec1f27;
    --card-black: #1b1c1e;
    --ink-white: #f2f2f2;
    --backdrop: #3a3b3d;
  }
  * { box-sizing: border-box; margin: 0; padding: 0; }
  html, body {
    width: 1200px;
    height: 1000px;
    overflow: hidden;
  }
  body {
    background: var(--backdrop);
    font-family: "Open Sans", Arial, sans-serif;
    display: flex;
    flex-direction: column;
    align-items: center;
    justify-content: center;
    gap: 60px;
  }
  .card {
    width: 700px;
    height: 400px;
    background: var(--card-black);
    border-radius: 4px;
    display: flex;
    align-items: center;
    justify-content: center;
  }
  .card-front .wordmark {
    display: flex;
    align-items: center;
    gap: 18px;
  }
  .wordmark-square {
    width: 34px;
    height: 34px;
    background: var(--brand-blue);
  }
  .wordmark-name {
    color: var(--ink-white);
    font-size: 68px;
    font-weight: 400;
    letter-spacing: 8px;
    text-transform: uppercase;
  }
  .card-back .contact {
    text-align: center;
    color: var(--ink-white);
    font-size: 17px;
    line-height: 1.45;
  }
  .contact-name {
    color: var(--brand-blue);
    font-size: 21px;
    font-weight: 700;
    text-transform: uppercase;
    line-height: 1.1;
  }
  .contact-title {
    color: var(--brand-red);
    font-size: 15px;
    font-weight: 400;
    text-transform: uppercase;
    letter-spacing: 0.5px;
  }
  .contact-rule {
    width: 135px;
    height: 1px;
    background: var(--ink-white);
    margin: 6px auto 8px;
  }
  .contact-label {
    color: var(--brand-blue);
    font-weight: 700;
  }
</style>
</head>
<body>
  <section class="card card-front">
    <div class="wordmark">
      <span class="wordmark-square"></span>
      <span class="wordmark-name">Tandrel</span>
    </div>
  </section>

  <section class="card card-back">
    <div class="contact">
      <p class="contact-name">Mara Lind</p>
      <p class="contact-title">President</p>
      <div class="contact-rule"></div>
      <p class="contact-address">2170 Halden Court Ashbury, NY 11402</p>
      <p class="contact-phones">
        <span class="contact-label">P:</span> 512 3408 7761
        <span class="contact-label">M:</span> 845 2290 6614
        <span class="contact-label">F:</span> 839 5127 4402
      </p>
      <p class="contact-web">
        <span class="contact-label">E:</span> mara@tandrelco.com
        <span class="contact-label">W:</span> www.tandrelco.com
      </p>
    </div>
  </section>
</body>
</html>
```